Standard Biz Card
Health Professionals
Please upload ai or eps of your logo
Kindly upload logo file in ai/eps format!
That contest is here: http://orders.markcraftplaza.example/contests/new-health-clinic-logo-biz-card
Sorry, there seem to be a misunderstandig as we thought this job was combined with the logo job. We do not have a logo yet, it is another contest going on at the moment.
Please upload the logo files

```html
<!DOCTYPE html>
<html lang="no">
<head>
<meta charset="utf-8">
<title>Business Card – Eirik Solberg, Manuelterapeut</title>
<link rel="stylesheet" href="https://fonts.googleapis.com/css2?family=Arimo:wght@400&family=Great+Vibes&display=swap">
<style>
  :root {
    --card: #ffffff;
    --ink: #111111;
    --link: #1a1aa6;
    --frame: #c9c9c9;
    --band-dark: #6e6e6e;
    --band-mid: #a3a3a3;
    --band-light: #e6e6e6;
    --foot: #e4e4e4;
    --logo-fill: #231f20;
    --logo-text: #f2f2f2;
  }
  html, body {
    margin: 0;
    padding: 0;
    width: 1200px;
    height: 721px;
    overflow: hidden;
    background: var(--card);
  }
  .card {
    position: relative;
    width: 1200px;
    height: 721px;
    box-sizing: border-box;
    background: var(--card);
    border: 5px solid var(--frame);
    border-bottom: none;
    font-family: "Arimo", Arial, sans-serif;
    color: var(--ink);
    overflow: hidden;
  }
  .card__bands {
    position: absolute;
    inset: 0;
    width: 1200px;
    height: 721px;
  }
  .contact {
    position: absolute;
    left: 64px;
    top: 188px;
  }
  .contact__address {
    margin: 0 0 14px;
    font-size: 31px;
    line-height: 1.2;
  }
  .contact__list {
    display: grid;
    grid-template-columns: auto auto;
    column-gap: 10px;
    margin: 0;
    font-size: 27px;
    line-height: 31px;
  }
  .contact__list dt { margin: 0; }
  .contact__list dt::after { content: ":"; margin-left: 8px; }
  .contact__list dd { margin: 0; }
  .contact__list a { color: var(--link); text-decoration: underline; }
  .logo-slot {
    position: absolute;
    left: 740px;
    top: 105px;
    width: 419px;
    height: 351px;
    box-sizing: border-box;
    border: 3px solid var(--frame);
    background: var(--card);
  }
  .logo-slot__mark {
    position: absolute;
    left: 22px;
    top: 22px;
    right: 22px;
    bottom: 22px;
    background: var(--logo-fill);
    display: flex;
    align-items: center;
    justify-content: center;
    text-align: center;
    color: var(--logo-text);
    font-size: 64px;
    line-height: 1.15;
  }
  .identity__name {
    position: absolute;
    left: 26px;
    top: 512px;
    margin: 0;
    font-size: 66px;
    font-weight: 400;
    letter-spacing: 1px;
    line-height: 1;
  }
  .identity__role {
    position: absolute;
    left: 74px;
    top: 598px;
    margin: 0;
    font-family: "Great Vibes", cursive;
    font-size: 44px;
    line-height: 1;
    color: var(--ink);
  }
</style>
</head>
<body>
<main class="card">
  <svg class="card__bands" viewBox="0 0 1200 721" aria-hidden="true">
    <defs>
      <linearGradient id="ribbon-grad" x1="0" y1="0" x2="1" y2="0">
        <stop offset="0" stop-color="var(--band-mid)"/>
        <stop offset="1" stop-color="var(--band-light)"/>
      </linearGradient>
      <linearGradient id="ribbon-shade" x1="0" y1="0" x2="0" y2="1">
        <stop offset="0" stop-color="#ffffff" stop-opacity="0.35"/>
        <stop offset="1" stop-color="#000000" stop-opacity="0.12"/>
      </linearGradient>
      <linearGradient id="title-band-grad" x1="0" y1="0" x2="1" y2="0">
        <stop offset="0" stop-color="#e9e9e9"/>
        <stop offset="1" stop-color="#b9b9b9"/>
      </linearGradient>
    </defs>
    <rect class="band band--foot" x="0" y="668" width="1200" height="53" fill="var(--foot)"/>
    <line x1="0" y1="668" x2="1200" y2="668" stroke="#cfcfcf" stroke-width="2"/>
    <rect class="band band--ribbon" x="645" y="546" width="555" height="78" fill="url(#ribbon-grad)"/>
    <rect x="645" y="546" width="555" height="78" fill="url(#ribbon-shade)"/>
    <rect class="band band--title" x="25" y="588" width="715" height="65" fill="url(#title-band-grad)"/>
    <polygon class="band band--fold" points="645,584 740,590 740,653" fill="var(--band-dark)"/>
    <line class="band band--rule" x1="25" y1="585" x2="645" y2="585" stroke="var(--band-dark)" stroke-width="5"/>
  </svg>

  <section class="contact">
    <p class="contact__address">Granlia 4, 1352 Kolsås</p>
    <dl class="contact__list">
      <dt>Phone</dt><dd>000.000.00</dd>
      <dt>Fax</dt><dd>000.000.000.0</dd>
      <dt>Email</dt><dd><a href="mailto:post@klinikkdemo.no">post@klinikkdemo.no</a></dd>
      <dt>Web</dt><dd>www.klinikkdemo.no</dd>
    </dl>
  </section>

  <div class="logo-slot">
    <div class="logo-slot__mark">your<br>logo<br>here</div>
  </div>

  <h1 class="identity__name">Eirik Solberg</h1>
  <p class="identity__role">Manuelterapeut</p>
</main>
</body>
</html>
```